Metal Warranty card design for Wristwatch brand

I will need a design for a warranty card that will be included with all of our watches. This card will be made from metal and will be rose gold plated. I have attached an example of our current card.

Website with our watch designs: www.pravonwatches.com

Target Market(s)

Men, 20-40s, watch collectors

Requirements
Must have
• Requires these fields and text (follow the example):
• Front:
• www.pravonwatches.com
• Back:
• 1 Year Limited Warranty
• Serial: (signature panel)
• Date: (Signature panel)
• Seller: (large panel)
Nice to have
• Cut outs, watch themed

```html
<!DOCTYPE html>
<html lang="en">
<head>
<meta charset="utf-8">
<title>Pravon Warranty Card</title>
<link href="https://fonts.googleapis.com/css2?family=Montserrat:wght@300;400;600&display=swap" rel="stylesheet">
<style>
  :root {
    --backdrop: #3b322d;
    --card-black: #050505;
    --steel: #a3a3a5;
    --steel-light: #d9d9db;
    --white: #ffffff;
    --ink: #1a1a1a;
  }
  html, body {
    margin: 0;
    padding: 0;
    width: 1200px;
    height: 831px;
    overflow: hidden;
    background: var(--backdrop);
    font-family: "Montserrat", Arial, sans-serif;
  }
  .card {
    position: absolute;
    top: 250px;
    width: 520px;
    height: 300px;
    background: var(--card-black);
    box-shadow: 0 10px 28px rgba(0,0,0,0.45);
    overflow: hidden;
  }
  .card--back { left: 50px; }
  .card--front { left: 630px; }

  .warranty-title {
    position: absolute;
    top: 26px;
    left: 120px;
    margin: 0;
    color: var(--white);
    font-weight: 300;
    font-size: 19px;
    letter-spacing: 1px;
  }
  .field-labels {
    position: absolute;
    top: 70px;
    left: 28px;
    color: var(--white);
    font-weight: 300;
    font-size: 18px;
    line-height: 26px;
    letter-spacing: 0.5px;
  }
  .field-panel {
    position: absolute;
    background: var(--white);
  }
  .field-panel--serial { top: 92px; left: 130px; width: 150px; height: 16px; }
  .field-panel--date { top: 124px; left: 120px; width: 150px; height: 16px; }
  .field-panel--seller { top: 156px; left: 112px; width: 150px; height: 88px; }

  .brand {
    position: absolute;
    right: 34px;
    bottom: 40px;
    display: flex;
    flex-direction: column;
    align-items: center;
    gap: 14px;
  }
  .brand-circle {
    width: 58px;
    height: 58px;
    border: 3px solid var(--white);
    border-radius: 50%;
    box-sizing: border-box;
  }
  .brand-name {
    color: var(--white);
    font-weight: 400;
    font-size: 44px;
    letter-spacing: 2px;
    line-height: 1;
  }

  .front-band {
    position: absolute;
    left: 0;
    bottom: 0;
    width: 100%;
    height: 62px;
    background: var(--steel);
  }
  .front-panel {
    position: absolute;
    top: 0;
    left: 0;
    width: 120px;
    height: 100%;
    background: var(--steel);
  }
  .website {
    position: absolute;
    left: 150px;
    bottom: 20px;
    margin: 0;
    color: var(--ink);
    font-weight: 600;
    font-size: 17px;
    letter-spacing: 5px;
  }
  .card--front .brand { bottom: 90px; right: 40px; }
  .card--front .brand-circle { border-color: var(--steel-light); }
  .card--front .brand-name { color: var(--steel-light); font-size: 50px; }
</style>
</head>
<body>
  <section class="card card--back" aria-label="Warranty card back">
    <h1 class="warranty-title">1 YEAR LIMITED WARRANTY</h1>
    <div class="field-labels">
      <div>SERIAL</div>
      <div>DATE</div>
      <div>SELLER</div>
    </div>
    <div class="field-panel field-panel--serial"></div>
    <div class="field-panel field-panel--date"></div>
    <div class="field-panel field-panel--seller"></div>
    <div class="brand">
      <div class="brand-circle"></div>
      <div class="brand-name">PRAVON</div>
    </div>
  </section>

  <section class="card card--front" aria-label="Warranty card front">
    <div class="front-panel"></div>
    <div class="front-band"></div>
    <div class="brand">
      <div class="brand-circle"></div>
      <div class="brand-name">PRAVON</div>
    </div>
    <p class="website">www.yourwebsite.com</p>
  </section>
</body>
</html>
```